Keto Food Brand Needs Packaging Design and Logo

We need a logo and packaging design for a stand-up food bag for our keto shake mix. We are a health and wellness brand launching our first shake mix product. I would like bold, bright colors. This document goes more in depth . This brand might encompass more than only food so I want the logo to be versatile for supplements and other health products. https://files.quarnix-docs.example/share/8hTzq3PmVx41KdLw92RaYcbE07nGsJuQfM5oXt2iHkAp/view?mode=sharing See images of logos attached. It doesn't have to be food for the logo but I like the creativity of the ones listed.

Target Market(s)

Keto. Health and Fitness

Logo Text

Trevalo

Font styles to use
Serif
Sans Serif

Colors

Designer to choose colors to be used in the design.

```html
<!DOCTYPE html>
<html lang="en">
<head>
<meta charset="utf-8">
<title>Trevalo Keto Cheesecake Shake Mix – Pouch Front</title>
<link rel="stylesheet" href="https://fonts.googleapis.com/css2?family=Fredoka:wght@600;700&family=Oswald:wght@500;600&display=swap">
<style>
  :root {
    --bg: #eeeeee;
    --foil-light: #f5f5f5;
    --foil-mid: #dedede;
    --turquoise: #2fc0d6;
    --turquoise-deep: #23b0c8;
    --ink: #262626;
    --navy: #163f50;
    --badge-red: #e3202a;
    --white: #ffffff;
    --cake-cream: #f6f0dc;
    --cake-crust: #b97a4c;
  }
  * { box-sizing: border-box; margin: 0; padding: 0; }
  html, body { width: 1126px; height: 1200px; overflow: hidden; }
  body { background: var(--bg); position: relative; }

  .pouch {
    position: absolute; left: 277px; top: 212px;
    width: 580px; height: 825px;
    background: linear-gradient(180deg, var(--turquoise) 0%, var(--turquoise-deep) 100%);
    border-radius: 8px 8px 12px 12px;
    overflow: hidden;
  }
  .seal-band {
    position: absolute; left: 0; top: 0; width: 100%; height: 115px;
    background: linear-gradient(180deg, var(--foil-light) 0%, var(--foil-mid) 100%);
  }
  .tear-mark {
    position: absolute; top: 96px;
    font-family: "Oswald", sans-serif; font-weight: 500;
    font-size: 11px; line-height: 12px; letter-spacing: 0.3px; color: var(--navy);
    display: flex; align-items: center; gap: 5px;
  }
  .tear-mark.left { left: 22px; }
  .tear-mark.right { right: 20px; }

  .brand {
    position: absolute; top: 228px; left: 0; width: 100%;
    text-align: center; line-height: 1;
    font-family: "Fredoka", sans-serif; font-weight: 600;
    font-size: 48px; color: var(--ink); letter-spacing: -0.5px;
  }
  .keto {
    position: absolute; left: 183px; top: 286px;
    font-family: "Fredoka", sans-serif; font-weight: 700;
    font-size: 213px; line-height: 169px; color: var(--ink);
    letter-spacing: -3px;
    transform: scaleX(0.88); transform-origin: left top;
  }
  .claims {
    position: absolute; left: 20px; top: 488px; width: 125px;
    font-family: "Oswald", sans-serif; font-weight: 500;
    font-size: 13px; line-height: 14px; color: var(--ink);
    text-align: center;
  }
  .claims li { list-style: none; padding: 3px 0; border-bottom: 1px solid var(--ink); }
  .claims li:last-child { border-bottom: none; }

  .cake-photo {
    position: absolute; left: 323px; top: 619px; width: 232px; height: 175px;
    border-radius: 30% 8% 18% 40%;
    background: linear-gradient(180deg, var(--white) 0%, var(--cake-cream) 55%, var(--cake-crust) 85%, #9a5c36 100%);
  }
  .servings-badge { position: absolute; left: 448px; top: 439px; width: 80px; height: 80px; }

  .flavor-name, .flavor-type {
    position: absolute; left: 37px; width: 500px; text-align: center;
    font-family: "Oswald", sans-serif; font-weight: 600;
    color: var(--navy); line-height: 1;
  }
  .flavor-name { top: 625px; font-size: 64px; }
  .flavor-type { top: 686px; font-size: 44px; }

  .net-weight, .supplement-note {
    position: absolute;
    font-family: "Oswald", sans-serif; font-weight: 500;
    color: var(--ink); line-height: 1;
  }
  .net-weight { left: 68px; top: 776px; font-size: 18px; }
  .supplement-note { left: 375px; top: 782px; font-size: 15px; letter-spacing: 0.4px; }
</style>
</head>
<body>
  <main class="pouch">
    <div class="seal-band">
      <span class="tear-mark left">
        <svg width="10" height="8" viewBox="0 0 12 10"><path d="M6 0 L12 10 L0 10 Z" fill="#163f50"/></svg>
        TEAR HERE
      </span>
      <span class="tear-mark right">
        RESEALABLE
        <svg width="12" height="9" viewBox="0 0 14 10"><path d="M0 0 L14 0 L7 10 Z" fill="#163f50"/></svg>
      </span>
    </div>

    <div class="brand">Trevalo</div>
    <h1 class="keto">KE<br>TO</h1>

    <ul class="claims">
      <li>NO ARTIFICIAL<br>FLAVORS</li>
      <li>ALL NATURAL</li>
      <li>KETO-FRIENDLY &amp;<br>LOW CARB</li>
    </ul>

    <div class="cake-photo" role="img" aria-label="Slice of cheesecake with a milk splash"></div>

    <svg class="servings-badge" viewBox="0 0 80 80" role="img" aria-label="20 servings">
      <circle cx="40" cy="40" r="38" fill="var(--badge-red)" stroke="#ffffff" stroke-width="2.5"/>
      <g transform="rotate(-18 40 40)" fill="#ffffff" text-anchor="middle" font-family="Fredoka, sans-serif" font-weight="700">
        <text x="40" y="41" font-size="26">20</text>
        <text x="40" y="57" font-size="12">SERVINGS</text>
      </g>
    </svg>

    <h2 class="flavor-name">CHEESECAKE</h2>
    <p class="flavor-type">SHAKE MIX</p>

    <p class="net-weight">Net Wt. 1.02 LB.</p>
    <p class="supplement-note">DIETARY SUPPLEMENT</p>
  </main>
</body>
</html>
```